Vornfield Business Cards

Logo files are included. Full "Vornfield" logo should be included on the back of the business card. The H symbol should be included on the front with the contact information.

Vornfield, LLC is the company name and we do commercial construction and real estate development consulting services. Look for a fairly simple card design utilizing our logo.

```html
<!DOCTYPE html>
<html lang="en">
<head>
<meta charset="utf-8">
<title>Vornfield Business Cards</title>
<link href="https://fonts.googleapis.com/css2?family=Poppins:wght@400;500;700&display=swap" rel="stylesheet">
<style>
  :root {
    --navy: #18374b;
    --gold: #e9ae20;
    --white: #ffffff;
    --backdrop: #e6e6e6;
  }
  * { margin: 0; padding: 0; box-sizing: border-box; }
  html, body { width: 1200px; height: 1085px; overflow: hidden; }
  body {
    position: relative;
    background: var(--backdrop);
    font-family: "Poppins", sans-serif;
  }
  .card {
    position: absolute;
    left: 301px;
    width: 579px;
    height: 343px;
    background: var(--navy);
    box-shadow: 2px 2px 0 rgba(0,0,0,0.75);
    overflow: hidden;
  }
  .card--front { top: 163px; }
  .card--back { top: 542px; }

  .holder-name {
    position: absolute; left: 37px; top: 36px;
    color: var(--gold); font-weight: 700; font-size: 21px; letter-spacing: 0.2px;
  }
  .holder-role {
    position: absolute; left: 37px; top: 58px;
    color: var(--white); font-size: 17px; font-weight: 400;
  }
  .contact-list {
    position: absolute; left: 37px; top: 180px; list-style: none;
    color: var(--white); font-size: 17px; line-height: 21px;
  }
  .contact-list li { display: flex; align-items: center; gap: 6px; }
  .contact-list svg { width: 15px; height: 15px; flex: none; }
  .address {
    position: absolute; left: 37px; top: 260px;
    display: flex; gap: 6px; color: var(--white); font-size: 17px; line-height: 21px;
  }
  .address svg { width: 15px; height: 18px; margin-top: 1px; flex: none; }

  .front-mark {
    position: absolute; left: 273px; top: 43px; width: 256px; height: 256px;
    border: 11px solid var(--white);
    border-radius: 50%;
    display: flex; align-items: center; justify-content: center;
  }
  .front-mark__name {
    color: var(--white); font-weight: 500; font-size: 32px; letter-spacing: 1px;
  }

  .back-ring {
    position: absolute; left: 231px; top: 60px; width: 116px; height: 116px;
    border: 6px solid var(--white); border-radius: 50%;
  }
  .back-name {
    position: absolute; left: 0; right: 0; top: 172px; text-align: center;
    color: var(--white); font-weight: 500; font-size: 57px; line-height: 70px; letter-spacing: 1px;
  }
  .web-band {
    position: absolute; left: 0; right: 0; top: 273px; height: 43px;
    background: var(--gold);
    display: flex; align-items: center; justify-content: center;
    color: var(--navy); font-weight: 500; font-size: 15px; letter-spacing: 4.5px;
  }
</style>
</head>
<body>
  <section class="card card--front">
    <h1 class="holder-name">DELMAR OKAFOR</h1>
    <p class="holder-role">Managing&nbsp; Director</p>
    <ul class="contact-list">
      <li>
        <svg viewBox="0 0 16 16"><path d="M3 1.5l3 3-1.6 1.6c.8 2 2.5 3.7 4.5 4.5L10.5 9l3 3-2 2C6.5 14 2 9.5 1 4z" fill="none" stroke="var(--gold)" stroke-width="1.6" stroke-linejoin="round"/></svg>
        044-987 210 553
      </li>
      <li>
        <svg viewBox="0 0 16 16"><rect x="1" y="3.5" width="14" height="9" fill="var(--gold)"/><path d="M1 3.5l7 5 7-5" fill="none" stroke="var(--navy)" stroke-width="1.2"/></svg>
        hello@vornfield.com
      </li>
      <li>
        <svg viewBox="0 0 16 16" fill="none" stroke="var(--gold)" stroke-width="1.3"><circle cx="8" cy="8" r="6.5"/><ellipse cx="8" cy="8" rx="3" ry="6.5"/><path d="M1.5 8h13M2.5 4.8h11M2.5 11.2h11"/></svg>
        www.vornfield.com
      </li>
    </ul>
    <div class="address">
      <svg viewBox="0 0 14 18"><path d="M7 1a5.5 5.5 0 0 1 5.5 5.5C12.5 11 7 17 7 17S1.5 11 1.5 6.5A5.5 5.5 0 0 1 7 1z" fill="var(--gold)"/><circle cx="7" cy="6.5" r="2" fill="var(--navy)"/></svg>
      <p>48, Larch Avenue<br>Country name, 123456</p>
    </div>
    <div class="front-mark">
      <span class="front-mark__name">VORNFIELD</span>
    </div>
  </section>

  <section class="card card--back">
    <div class="back-ring"></div>
    <h2 class="back-name">VORNFIELD</h2>
    <div class="web-band">WWW.VORNFIELD.COM</div>
  </section>
</body>
</html>
```